Refresh and update our Juice bottle label to a more vibrant and eye catching brand

We’ve had this label and included trademarked logo for the past 10 years. We do change the name of the juice ands its ingredients accordingly.
I want to up-date this round juice bottle label so it is more eye catching , trendy and clearly screams (healthy/juice/delicious/refreshing/beauty/youthful/high energy.
I have attached my trademarked logos as well as examples of a few labels. I also attached a few pictures of our juices with the current label which is a 2x4 inch front and back. I want you to see how colorful our juice is. I want the updated label to include out trademarked logo somehow but add in some color or graphics that speak to the message above in (). Open to adding color and even having a wrap around label instead of front and back=

Target Market(s)

Upscale women:men, age 20-65 40:30 ratio, health/ fitness/ body aware, anti aging/ high energy/ prevention of disease. Clientele is primarily caucasian.

Industry/Entity Type

Beverage, cold-pressed juice, wellness

Font styles to use
Sans Serif

Colors
59FF00
82FF00
B8FF75
E3FFCB
F4FFEA
EB3D1F
EC4F4E
F09395
F8D3D4
FCEDEE
E54698
E96AAD
F1A4CE
F9D9EA
FCEFF6
6B429C
8869AF
B7A5CE
E3DAEB
F3F0F8

Requirements
Must have
• My trademarked logo incorporated somehow. Bright/simple/modern/trendy style. I need to be able to change out the name of the juice and its ingredients and nutritional information. I want the label to say “100% Juice” basically this all needs to be on it: Name and Address. The name and address of your juicing business. ... Name of the Food. You should list the name of the food that is commonly used. ... What is the Amount of Juice inside of the bottle? ... % of juice declaration. ... Ingredients. ... Food Allergen (made in a facility with nuts). ... The Disclaimer. Must say “cold-pressed juice”
Nice to have
• Maybe a graphic image of a piece of fruit like a lemon with sliced cucumbers, I want vibrant colors added such as maybe use hot pink -outline or graphic on my Feel Rosy Bright? since the juice is pink. Or a bright yellow on my Zest Rising? Or a bright green on Lush Ace. Maybe some wording like “no added sugar or preservatives”, “gluten free”
Should not have
• No health guarantees

```html
<!DOCTYPE html>
<html lang="en">
<head>
<meta charset="utf-8">
<title>Zest Rising? – Leafline Juicery Bottle Label</title>
<link rel="stylesheet" href="https://fonts.googleapis.com/css2?family=Lilita+One&family=Montserrat:wght@500;700;800&display=swap">
<style>
  :root {
    --backdrop: #98d6a0;
    --cream: #f4ffea;
    --mint: #e3ffcb;
    --lime-soft: #b8ff75;
    --lime: #82ff00;
    --lime-hot: #59ff00;
    --leaf-dark: #0e6a2f;
    --leaf-deep: #0b5a27;
    --leaf-brand: #4fb800;
    --ink: #1d3b26;
    --white: #ffffff;
  }
  * { margin: 0; padding: 0; box-sizing: border-box; }
  html, body {
    width: 1016px;
    height: 1200px;
    overflow: hidden;
    background: var(--backdrop);
  }
  .label {
    position: absolute;
    left: 58px;
    top: 150px;
    width: 900px;
    height: 900px;
  }
  .brand-name {
    font-family: "Montserrat", sans-serif;
    font-weight: 800;
    font-size: 50px;
    fill: var(--leaf-brand);
  }
  .headline {
    font-family: "Lilita One", sans-serif;
    font-size: 104px;
    fill: var(--white);
    stroke: var(--leaf-dark);
    stroke-width: 14px;
    stroke-linejoin: round;
    paint-order: stroke fill;
  }
  .ingredient {
    font-family: "Lilita One", sans-serif;
    font-size: 32px;
    fill: var(--cream);
  }
  .freshness {
    font-family: "Lilita One", sans-serif;
    font-size: 29px;
    fill: var(--leaf-deep);
  }
  .juice-claim {
    font-family: "Montserrat", sans-serif;
    font-weight: 800;
    font-size: 20px;
    fill: var(--leaf-dark);
  }
  .fine-print {
    font-family: "Montserrat", sans-serif;
    font-weight: 500;
    font-size: 12.5px;
    fill: var(--ink);
  }
  .allergen {
    font-weight: 700;
  }
  .web {
    font-family: "Montserrat", sans-serif;
    font-weight: 700;
    font-size: 18px;
    fill: var(--leaf-brand);
  }
</style>
</head>
<body>
  <svg class="label" viewBox="0 0 800 800" role="img" aria-label="Zest Rising? round cold-pressed juice bottle label by Leafline Juicery">
    <defs>
      <clipPath id="label-edge"><circle cx="400" cy="400" r="400"/></clipPath>
      <linearGradient id="band-glow" x1="0" y1="0" x2="1" y2="0">
        <stop offset="0" stop-color="#3aa800"/>
        <stop offset="0.5" stop-color="#82ff00"/>
        <stop offset="1" stop-color="#2f9a12"/>
      </linearGradient>
      <radialGradient id="deep-band" cx="0.5" cy="0.2" r="0.7">
        <stop offset="0" stop-color="#2a9a2a"/>
        <stop offset="1" stop-color="#0b5a27"/>
      </radialGradient>
      <symbol id="leaf-mark" viewBox="0 0 40 30">
        <path d="M2 4 C18 0 36 8 38 26 C22 28 6 20 2 4 Z" fill="#82ff00"/>
        <path d="M6 7 C16 12 26 18 34 24" stroke="#0e6a2f" stroke-width="2" fill="none"/>
      </symbol>
    </defs>

    <g clip-path="url(#label-edge)">
      <rect class="label-base" width="800" height="800" fill="var(--cream)"/>
      <path class="headline-band" d="M0 170 Q400 360 800 170 L800 800 L0 800 Z" fill="url(#band-glow)" stroke="var(--leaf-dark)" stroke-width="7"/>
      <path class="ingredient-band" d="M0 520 Q400 330 800 520 L800 800 L0 800 Z" fill="url(#deep-band)" stroke="var(--lime-soft)" stroke-width="6"/>
      <rect class="info-panel" x="0" y="588" width="800" height="212" fill="var(--cream)"/>
    </g>

    <!-- brand -->
    <circle class="brand-dot" cx="220" cy="138" r="30" fill="var(--lime)"/>
    <text class="brand-name" x="268" y="128">Leafline</text>
    <text class="brand-name" x="268" y="182">Juicery</text>

    <!-- juice name -->
    <text class="headline" x="400" y="368" text-anchor="middle" textLength="680" lengthAdjust="spacingAndGlyphs">ZEST RISING?</text>

    <!-- ingredients -->
    <g class="ingredients">
      <use href="#leaf-mark" x="148" y="462" width="38" height="28"/>
      <text class="ingredient" x="200" y="490">PINEAPPLE</text>
      <use href="#leaf-mark" x="380" y="462" width="38" height="28"/>
      <text class="ingredient" x="432" y="490">FUJI APPLE</text>
      <use href="#leaf-mark" x="148" y="507" width="38" height="28"/>
      <text class="ingredient" x="200" y="535">LEMON</text>
      <use href="#leaf-mark" x="380" y="507" width="38" height="28"/>
      <text class="ingredient" x="432" y="535">TURMERIC ROOT</text>
    </g>

    <!-- freshness pill -->
    <rect class="freshness-pill" x="76" y="561" width="650" height="48" rx="24" fill="var(--lime)" stroke="var(--leaf-dark)" stroke-width="3"/>
    <text class="freshness" x="401" y="595" text-anchor="middle">BEST IF USED WITHIN 5 DAYS OF PURCHASE</text>

    <!-- info -->
    <text class="juice-claim" x="400" y="638" text-anchor="middle">100% COLD-PRESSED VEGETABLE &amp; FRUIT JUICE</text>
    <g class="fine-print" text-anchor="middle">
      <text x="400" y="658">Perishable Keep Refrigerated Shake Well *separation is natural*</text>
      <text x="400" y="672">WARNING: This product has not been pasteurized and, therefore may contain</text>
      <text x="400" y="686">harmful bacteria that can cause serious illness in children, the elderly,</text>
      <text x="400" y="700">and persons with weakened immune systems.</text>
      <text class="allergen" x="400" y="714">Made in a facility that processes tree nuts.</text>
      <text x="400" y="728">Net Wt. 12oz (354mL)</text>
      <text x="400" y="742">4410 Orchard Ln #8, Fairview,CA 90210</text>
    </g>
    <text class="web" x="400" y="768" text-anchor="middle">leaflinejuicery.com</text>
  </svg>
</body>
</html>
```